依頼詳細
全国の医科大学の掲示板と、汎療競のHPに掲載されます。医学生が地方の大会を勝ち抜いて汎療競に参加したくなるような、熱く燃えるようなポスターデザインをお待ちしております。
記載項目
第55回汎国療徒競技祭頂点争奪戦
卓球、軟式テニス、バドミントン、バレーボール、バスケットボール、サッカー、弓道、柔道
http://www.hanryokyo.kumoyado.example/top.htmと添付ファイルのQRコード
主管:北杜薬科大学 主催:北陽療徒競技協会、南陽療徒競技協会
サイズ
A2
ページ数
片面
希望イメージ
シンプル 複雑
単色 カラフル
暗い 明るい
日常 高級
遊び心 厳粛
未来的 伝統的
女性的 男性的
希望する色
赤系、黄・オレンジ系、無彩色系、青も欲しいです。
納品ファイル
• 高解像度JPG (.jpg)
• PNG形式 (.png)
補足説明
なるべく1月末までに仕上げて下さると嬉しいです。
■ 選んだ理由

色彩が大変気に入りました。また、王座決定戦の字がとても気に入りました。

■ 提案者全員のお礼・コメント

沢山素敵なポスターを提案してくださり、ありがとうございます。

```html
<!DOCTYPE html>
<html lang="ja">
<head>
<meta charset="utf-8">
<title>第55回汎国療徒競技祭 頂点争奪戦</title>
<link rel="stylesheet" href="https://fonts.googleapis.com/css2?family=Noto+Serif+JP:wght@700;900&family=Noto+Sans+JP:wght@500;700;900&family=Yuji+Boku&display=swap">
<style>
  :root{
    --paper:#ffffff;
    --ink:#111111;
    --red:#d7141c;
    --hot-red:#ff2a1f;
    --band:#0d0d0d;
    --grey:#555555;
    --blue:#2a6fe0;
    --cyan:#22b8e8;
    --magenta:#e8247f;
    --purple:#8a3ad0;
    --orange:#ff8a12;
    --yellow:#ffd81a;
    --green:#2fb860;
  }
  *{margin:0;padding:0;box-sizing:border-box}
  html,body{width:848px;height:1200px;overflow:hidden;background:var(--paper)}
  .poster{position:relative;width:848px;height:1200px;background:var(--paper);overflow:hidden}

  .athletes-art{
    position:absolute;left:150px;top:0;width:698px;height:720px;
    background:
      radial-gradient(ellipse 18% 14% at 60% 14%, var(--magenta) 0 35%, transparent 72%),
      radial-gradient(ellipse 20% 16% at 82% 22%, var(--cyan) 0 30%, transparent 72%),
      radial-gradient(ellipse 22% 18% at 48% 32%, var(--purple) 0 35%, transparent 74%),
      radial-gradient(ellipse 20% 16% at 28% 42%, var(--blue) 0 35%, transparent 72%),
      radial-gradient(ellipse 24% 18% at 66% 46%, var(--hot-red) 0 38%, transparent 74%),
      radial-gradient(ellipse 22% 16% at 84% 58%, var(--orange) 0 35%, transparent 72%),
      radial-gradient(ellipse 22% 16% at 44% 62%, var(--orange) 0 30%, transparent 72%),
      radial-gradient(ellipse 20% 14% at 58% 76%, var(--yellow) 0 35%, transparent 72%),
      radial-gradient(ellipse 18% 14% at 22% 74%, var(--green) 0 35%, transparent 72%),
      radial-gradient(ellipse 16% 12% at 38% 88%, var(--magenta) 0 30%, transparent 72%),
      radial-gradient(ellipse 14% 10% at 74% 88%, var(--hot-red) 0 30%, transparent 72%),
      radial-gradient(ellipse 48% 46% at 54% 50%, rgba(255,120,60,.35), transparent 80%);
  }

  .tagline{
    position:absolute;left:58px;top:36px;z-index:2;
    writing-mode:vertical-rl;
    font-family:"Noto Serif JP",serif;font-weight:900;font-size:40px;letter-spacing:4px;
    color:var(--ink);
  }
  .tagline .accent{color:var(--red);font-size:52px}

  .edition-badge{
    position:absolute;left:72px;top:684px;width:108px;height:108px;border-radius:50%;
    background:var(--red);color:#fff;z-index:3;
    display:flex;align-items:center;justify-content:center;
    font-family:"Noto Sans JP",sans-serif;font-weight:900;font-size:32px;letter-spacing:-1px;
  }
  .edition-badge small{font-size:20px}

  .event-band{
    position:absolute;left:96px;top:752px;width:690px;height:84px;z-index:2;
    background:var(--band);transform:skewX(-8deg);
    display:flex;align-items:center;justify-content:center;
  }
  .event-band span{
    transform:skewX(8deg);color:#fff;
    font-family:"Noto Sans JP",sans-serif;font-weight:900;font-size:56px;letter-spacing:6px;
  }

  .title-main{
    position:absolute;left:0;right:0;top:850px;text-align:center;
    font-family:"Yuji Boku",serif;font-weight:400;font-size:160px;line-height:1.1;
    color:var(--red);letter-spacing:-10px;
  }

  .sports-list{
    position:absolute;left:0;right:0;top:1066px;text-align:center;
    font-family:"Noto Sans JP",sans-serif;font-weight:700;font-size:15px;color:var(--ink);
  }
  .sports-list i{font-style:normal;color:var(--grey);margin:0 7px}

  .organizers{
    position:absolute;left:0;right:0;top:1122px;text-align:center;
    font-family:"Noto Sans JP",sans-serif;font-weight:500;font-size:11px;color:var(--ink);
  }
  .site-url{
    position:absolute;left:0;right:0;top:1146px;text-align:center;
    font-family:"Noto Sans JP",sans-serif;font-weight:900;font-size:18px;color:var(--red);
  }

  .qr-code{
    position:absolute;left:758px;top:1100px;width:72px;height:72px;
    border:3px solid var(--ink);background:var(--paper);
  }
</style>
</head>
<body>
<main class="poster">
  <div class="athletes-art" role="img" aria-label="赤・橙・黄・紫・青の水彩のしぶきが炎のように燃え立つ中、躍動する卓球・テニス・バドミントン・バレーボール・バスケットボール・サッカー・弓道・柔道の選手たちのシルエット"></div>

  <p class="tagline">スポーツの<span class="accent">頂点</span>をめざせ。</p>

  <div class="edition-badge"><small>第</small>55<small>回</small></div>
  <div class="event-band"><span>汎国療徒競技祭</span></div>
  <h1 class="title-main">頂点争奪戦</h1>

  <p class="sports-list">卓球<i>/</i>軟式テニス<i>/</i>バドミントン<i>/</i>バレーボール<i>/</i>バスケットボール<i>/</i>サッカー<i>/</i>弓道<i>/</i>柔道</p>

  <p class="organizers">主管：北杜薬科大学　主催：北陽療徒競技協会、南陽療徒競技協会</p>
  <p class="site-url">http://www.hanryokyo.kumoyado.example/top.htm</p>

  <div class="qr-code" role="img" aria-label="大会サイトへのQRコード"></div>
</main>
</body>
</html>
```